2022 American Football Calendar Design

This project is for an American High School Football calendar for 2022.

The theme is US football and specifically high-school football for a streaming TV show about American high-school football.

The total number of pages will be 28 with the cover being 4 pages and the months being the other 24 pages.

Design Elements:

1. Each month will have 2 pages. 1 for the lead / hero image and one for the days of the month.

2. We will supply the images for each month of the calendar. There may be multiple potential image options for a given month. You can, as the designer, choose to use one or multiple images for the month if you feel the design would benefit.

3. Each month will have special days including US Holidays and special Football Days. We will supply a spreadsheet with all of these days and dates.

4. The boxes for the days should be square with enough space to allow for writing in the box when the calendar is printed.

5. Each month will also have a special quote text area that will contain special informational or an inspirational quote.

6. The calendar dimensions are 11" x 8 1/2" (US Letter - landscape orientation) - folded. So each page is US Letter size. A print guide template is attached from the printing company.

7. The title of the calendar is Pinebrook Rally 2022 Calendar.

For this contest please supply design concepts for the following:
1. Cover page;
2. Inside page;
3. Month Hero page;
4. Days of the month page;
5. Back cover page;

We will use these design concepts to choose the winner who will then need to finish the complete calendar design and preparation for printing.

Final Deliverables:

A. Complete 28 page calendar design - the winner will complete the design and layout of all pages.

B. Final print ready PDF at least 350 dpi with bleed for printing. Please see the attached size template from the printing company with guides.

C. Layered & Fully Editable Source File - InDesign, AI or PSD (NO COREL DRAW PLEASE - Adobe products only please). If vector files are supplied, we will also need a text editable version.

D. Any fonts used - we have licensing, if needed, available from Quillon Type and Marvesta Assets.

We are looking for a fast turnaround on this project so it can be sent to the printer next week.

Target Market(s)

High-school football players and their family & friends

Industry/Entity Type

American football

Font styles to use
Other font styles liked:
• Collegiate type sports fonts.

Colors

Designer to choose colors to be used in the design.

Requirements
Must have
• 350 DPI print-ready PDF, Fully editable source files including fonts & layers (NO Corel Draw) - see brief
Nice to have
• vector (AI) and PSD
Should not have
• Do not use Corel Draw

```html
<!DOCTYPE html>
<html lang="en">
<head>
<meta charset="utf-8">
<title>Pinebrook Rally 2022 Calendar – Covers</title>
<link rel="stylesheet" href="https://fonts.googleapis.com/css2?family=Graduate&family=Montserrat:wght@600;700&display=swap">
<style>
  :root {
    --canvas: #f2f2f2;
    --maroon: #6e1a1c;
    --maroon-deep: #3e0d0f;
    --maroon-dark: #2a0708;
    --red-glow: #b3372c;
    --ink: #0c0c0c;
    --white: #ffffff;
    --smoke: #d9d9d9;
  }
  * { margin: 0; padding: 0; box-sizing: border-box; }
  html, body { width: 900px; height: 1200px; overflow: hidden; background: var(--canvas); }
  body { position: relative; font-family: "Montserrat", Arial, sans-serif; }

  .page {
    position: absolute;
    left: 100px;
    width: 700px;
    height: 541px;
    overflow: hidden;
    box-shadow: 0 10px 24px rgba(0,0,0,.28);
  }
  .page--front { top: 39px; background: var(--ink); }
  .page--back  { top: 620px; }
  .page svg.art { position: absolute; inset: 0; width: 100%; height: 100%; }

  .cover-title {
    position: absolute;
    right: 24px;
    top: 88px;
    width: 372px;
    text-align: center;
    font-family: "Graduate", "Georgia", serif;
    color: var(--white);
    line-height: 1;
  }
  .cover-title__name { display: block; font-size: 27px; letter-spacing: .5px; text-shadow: 2px 2px 0 var(--maroon-dark); }
  .cover-title__year {
    display: block; font-size: 132px; letter-spacing: -2px; margin-top: 2px;
    -webkit-text-stroke: 3px var(--maroon-dark);
    paint-order: stroke fill;
    text-shadow: 4px 4px 0 var(--maroon-dark);
  }
  .cover-title__word {
    display: block; font-size: 56px; margin-top: 2px;
    -webkit-text-stroke: 2px var(--maroon-dark);
    paint-order: stroke fill;
    text-shadow: 3px 3px 0 var(--maroon-dark);
  }

  .socials { position: absolute; display: flex; justify-content: center; align-items: center; }
  .social { display: flex; align-items: center; color: var(--white); font-weight: 700; white-space: nowrap; }
  .social__dot { border-radius: 50%; background: var(--white); flex: none; }
  .website { position: absolute; color: var(--white); font-weight: 600; text-align: center; white-space: nowrap; }

  .page--front .socials { left: 300px; width: 220px; top: 466px; gap: 10px; }
  .page--front .social { font-size: 9px; gap: 4px; }
  .page--front .social__dot { width: 18px; height: 18px; }
  .page--front .website { left: 290px; width: 240px; top: 496px; font-size: 8px; letter-spacing: 4px; }

  .page--back .socials { left: 0; width: 700px; top: 430px; gap: 18px; }
  .page--back .social { font-size: 13px; gap: 7px; }
  .page--back .social__dot { width: 42px; height: 42px; }
  .page--back .website { left: 0; width: 700px; top: 490px; font-size: 9px; letter-spacing: 4.5px; }
</style>
</head>
<body>

<section class="page page--front" aria-label="Front cover">
  <svg class="art" viewBox="0 0 700 541" preserveAspectRatio="none">
    <defs>
      <linearGradient id="panelRed" x1="0" y1="0" x2="1" y2="1">
        <stop offset="0" stop-color="#7c2220"/>
        <stop offset="1" stop-color="#4a1012"/>
      </linearGradient>
      <radialGradient id="stadiumGlow" cx="0.85" cy="0.12" r="0.35">
        <stop offset="0" stop-color="#f0a070" stop-opacity=".85"/>
        <stop offset=".5" stop-color="#b3372c" stop-opacity=".35"/>
        <stop offset="1" stop-color="#7c2220" stop-opacity="0"/>
      </radialGradient>
      <linearGradient id="playerTone" x1="0" y1="0" x2="0" y2="1">
        <stop offset="0" stop-color="#e2e2e2"/>
        <stop offset=".35" stop-color="#c85a3e"/>
        <stop offset=".75" stop-color="#9c2620"/>
        <stop offset="1" stop-color="#1d2230"/>
      </linearGradient>
    </defs>
    <polygon class="cover-panel" points="340,0 700,0 700,345 290,440" fill="url(#panelRed)"/>
    <polygon class="cover-lights" points="340,0 700,0 700,345 290,440" fill="url(#stadiumGlow)" role="img" aria-label="Glowing stadium floodlights"/>
    <polygon class="cover-stripe" points="290,440 700,345 700,367 284,462" fill="var(--white)"/>
    <polygon class="cover-corner" points="548,541 700,541 700,418" fill="var(--white)"/>
    <polygon class="cover-photo" points="0,0 340,0 300,430 275,541 0,541" fill="url(#playerTone)" role="img" aria-label="Football player in red jersey and helmet gripping the ball"/>
  </svg>

  <h1 class="cover-title">
    <span class="cover-title__name">PINEBROOK RALLY</span>
    <span class="cover-title__year">2022</span>
    <span class="cover-title__word">CALENDAR</span>
  </h1>

  <div class="socials">
    <span class="social"><span class="social__dot"></span>Snapline</span>
    <span class="social"><span class="social__dot"></span>Huddle</span>
    <span class="social"><span class="social__dot"></span>Fieldpost</span>
  </div>
  <p class="website">WWW.PINEBROOKRALLY.COM</p>
</section>

<section class="page page--back" aria-label="Back cover">
  <svg class="art" viewBox="0 0 700 541" preserveAspectRatio="none">
    <defs>
      <linearGradient id="backTone" x1="0" y1="0" x2="0" y2="1">
        <stop offset="0" stop-color="#4a1012"/>
        <stop offset=".45" stop-color="#7a2a28"/>
        <stop offset=".6" stop-color="#6e2322"/>
        <stop offset="1" stop-color="#6a1b1d"/>
      </linearGradient>
    </defs>
    <rect class="back-photo" width="700" height="541" fill="url(#backTone)" role="img" aria-label="Maroon-tinted photo of a young player walking down a small-town road"/>
  </svg>

  <div class="socials">
    <span class="social"><span class="social__dot"></span>Snapline</span>
    <span class="social"><span class="social__dot"></span>Huddle</span>
    <span class="social"><span class="social__dot"></span>Fieldpost</span>
  </div>
  <p class="website">WWW.PINEBROOKRALLY.COM</p>
</section>

</body>
</html>
```